Saffron Lantern Court Business Card

I am looking for a business card desgined for my restaurant. It is an Indian restaurant, we are looking for something thats modern, yet traditional with the indian culture, we are looking for colors that match our logo. The logo is a design of the building with the name of the restaurant. for more information on the restaurant go to www.saffronlanterncourt.example

Industry/Entity Type

Indian Restaurant

Contact Information for Business Card

we are looking for somthing thats modern, yet traditional with the indian culture, we are looking for colors that match our logo. The logo is a design of the building with the name of the restaurant. for more information on the restaurant go to www.saffronlanterncourt.example

Requirements
Must have
• The logo that is attached,
• Name: Harvinder Oberoi,
• address of the restaurant: 7328 West Larkspur Rd, Phoenix, Arizona, 85213
• Phone: (602) 555-0147
• Fax: (602) 555-0193
• Restaurant Catering Banquet
• Website: www.SaffronLanternCourt.example
Nice to have
• wanted to get something that goes with the theme of the restaurant, which is traditional but also keep a very professional and modern touch

```html
<!DOCTYPE html>
<html lang="en">
<head>
<meta charset="utf-8">
<title>Saffron Lantern Court – Business Card</title>
<link rel="stylesheet" href="https://fonts.googleapis.com/css2?family=Caveat+Brush&family=Tenor+Sans&family=Libre+Baskerville:wght@700&family=Montserrat:wght@700&display=swap">
<style>
  :root {
    --paper: #ffffff;
    --card-yellow: #fad55c;
    --card-yellow-light: #fde38a;
    --card-yellow-deep: #f3c74a;
    --ornament-tone: rgba(222, 170, 60, 0.35);
    --text-maroon: #9a2430;
    --label-ink: #111111;
  }
  * { box-sizing: border-box; margin: 0; padding: 0; }
  html, body {
    width: 933px;
    height: 1200px;
    overflow: hidden;
    background: var(--paper);
  }
  .sheet {
    position: relative;
    width: 933px;
    height: 1200px;
  }
  .side-label {
    position: absolute;
    left: 99px;
    font-family: "Libre Baskerville", serif;
    font-weight: 700;
    font-size: 28px;
    color: var(--label-ink);
    letter-spacing: 0.5px;
  }
  .side-label--front { top: 93px; }
  .side-label--back { top: 615px; }

  .card {
    position: absolute;
    left: 99px;
    width: 735px;
    height: 441px;
    overflow: hidden;
    background:
      radial-gradient(ellipse at 50% 40%, var(--card-yellow-light) 0%, var(--card-yellow) 55%, var(--card-yellow-deep) 100%);
  }
  .card--front { top: 138px; }
  .card--back { top: 661px; }

  .ornament {
    position: absolute;
    border-radius: 50%;
    background: radial-gradient(circle, var(--ornament-tone) 0%, rgba(222,170,60,0.18) 55%, rgba(222,170,60,0) 72%);
  }
  .ornament--tl { left: -80px; top: -60px; width: 260px; height: 260px; }
  .ornament--bl { left: -80px; top: 250px; width: 260px; height: 260px; }
  .ornament--tr { right: -80px; top: -60px; width: 260px; height: 260px; }
  .ornament--br { right: -80px; top: 250px; width: 260px; height: 260px; }
  .ornament--back { left: -90px; top: -40px; width: 500px; height: 500px; }

  .brand-lockup {
    position: absolute;
    left: 0;
    right: 0;
    top: 95px;
    text-align: center;
  }
  .brand-name {
    font-family: "Tenor Sans", sans-serif;
    font-size: 58px;
    line-height: 72px;
    color: var(--text-maroon);
    letter-spacing: 3px;
    text-transform: uppercase;
  }
  .brand-since {
    margin-top: 22px;
    font-family: "Montserrat", sans-serif;
    font-weight: 700;
    font-size: 15px;
    letter-spacing: 3.5px;
    color: var(--text-maroon);
  }

  .back-content {
    position: absolute;
    inset: 0;
    text-align: center;
    color: var(--text-maroon);
  }
  .back-title {
    position: absolute;
    left: 0; right: 0;
    top: 26px;
    font-family: "Caveat Brush", cursive;
    font-size: 62px;
    line-height: 70px;
  }
  .back-services {
    position: absolute;
    left: 0; right: 0;
    top: 98px;
    font-family: "Caveat Brush", cursive;
    font-size: 30px;
    line-height: 34px;
  }
  .welcome {
    position: absolute;
    left: 0; right: 0;
    top: 170px;
    font-family: "Tenor Sans", sans-serif;
    font-size: 25px;
    line-height: 29px;
  }
  .address {
    position: absolute;
    left: 0; right: 0;
    top: 257px;
    font-family: "Tenor Sans", sans-serif;
    font-size: 25px;
  }
  .phone-row {
    position: absolute;
    left: 50px;
    right: 52px;
    top: 310px;
    display: flex;
    justify-content: space-between;
    font-family: "Tenor Sans", sans-serif;
    font-size: 25px;
  }
  .website {
    position: absolute;
    left: 0; right: 0;
    top: 360px;
    font-family: "Tenor Sans", sans-serif;
    font-size: 33px;
  }
</style>
</head>
<body>
<main class="sheet">
  <h2 class="side-label side-label--front">FRONT</h2>
  <section class="card card--front">
    <div class="ornament ornament--tl" role="img" aria-label="Faint mandala ornament"></div>
    <div class="ornament ornament--bl" role="img" aria-label="Faint mandala ornament"></div>
    <div class="ornament ornament--tr" role="img" aria-label="Faint mandala ornament"></div>
    <div class="ornament ornament--br" role="img" aria-label="Faint mandala ornament"></div>
    <div class="brand-lockup">
      <h1 class="brand-name">Saffron<br>Lantern<br>Court</h1>
      <p class="brand-since">SINCE 1985</p>
    </div>
  </section>

  <h2 class="side-label side-label--back">BACK</h2>
  <section class="card card--back">
    <div class="ornament ornament--back" role="img" aria-label="Large faint mandala ornament"></div>
    <div class="back-content">
      <p class="back-title">Saffron Lantern Court</p>
      <p class="back-services">Restaurant · Catering · Banquet</p>
      <p class="welcome">Harvinder Oberoi and his friendly<br>team welcome you</p>
      <p class="address">7328 West Larkspur Rd, Phoenix, Arizona, 85213</p>
      <p class="phone-row"><span>Phone: (602) 555-0147</span><span>Fax: (602) 555-0193</span></p>
      <p class="website">www.SaffronLanternCourt.example</p>
    </div>
  </section>
</main>
</body>
</html>
```